Design concept for PixelHarbor.com Support Page

We are about to launch a new support page for our www.pixelharbor.example service for photographers and visual artists. The service provides media management, cloud storage, promotional and secure distribution to our members.

The support page will include FAQs and video tutorials.

In particular we're looking for a header for this page that suggests the user is in the support area of our service - so perhaps an illustration that suggests support could look nice (perhaps repair man or doctor iconography). Something to give this area of our site a different look and something that looks both cool and friendly.

Currently the page looks distinctly sparse and undesigned (see attached screenshot) - something that could be remedied, we feel, by some subtle design enhancements that we can implement using CSS.

```html
<!DOCTYPE html>
<html lang="en">
<head>
<meta charset="utf-8">
<title>PixelHarbor Support</title>
<link href="https://fonts.googleapis.com/css2?family=Open+Sans:wght@300;400;600;700&display=swap" rel="stylesheet">
<style>
:root{
  --page:#f7f7f7;
  --band:#efefef;
  --orange:#f26a1b;
  --orange-dark:#d9560c;
  --ink:#2b2b2b;
  --text:#3a3a3a;
  --muted:#666;
  --rule:#dcdcdc;
  --card-top:#ffffff;
  --card-bottom:#efefef;
  --card-border:#e2e2e2;
}
*{box-sizing:border-box;margin:0;padding:0}
html,body{width:837px;height:1200px;overflow:hidden}
body{background:var(--page);font-family:"Open Sans",Arial,sans-serif;color:var(--text);position:relative}

.site-header{position:absolute;left:0;top:0;width:837px;height:72px;background:var(--band)}
.brand{position:absolute;left:108px;top:25px;display:flex;align-items:center;gap:7px;font-size:21px;font-weight:600;color:#4a4f57;letter-spacing:-.3px}
.brand-mark{width:20px;height:20px;border-radius:50%;background:#4a4f57}
.live-support{position:absolute;left:618px;top:30px;width:104px;height:24px;background:var(--orange);border-bottom:2px solid var(--orange-dark);color:#fff;font-size:9px;display:flex;align-items:center;justify-content:center;gap:4px;text-transform:uppercase}
.live-support .caret{width:9px;height:9px;background:#fff;display:inline-block;position:relative}
.live-support .caret::after{content:"";position:absolute;left:2px;top:3px;border:2.5px solid transparent;border-top:3px solid var(--orange)}

.hero{position:absolute;left:106px;top:90px;width:621px;height:200px;background:#f5f5f5;border:1px solid #ececec}
.hero-art{position:absolute;background:linear-gradient(180deg,#f6bd4f 0%,#2e8a8f 70%,#c6cbb9 100%);border-radius:40px 40px 6px 6px}
.hero-art.left{left:38px;top:28px;width:84px;height:150px}
.hero-art.right{left:398px;top:10px;width:176px;height:189px;background:linear-gradient(180deg,#e9e9e9 0%,#f6bd4f 40%,#2e8a8f 100%);border-radius:80px 80px 0 0}
.hero-title{position:absolute;left:137px;top:103px;font-weight:300;font-size:25px;color:var(--ink);line-height:1}
.hero-title strong{color:var(--orange);font-weight:600}
.hero-sub{position:absolute;left:141px;top:134px;font-weight:300;font-size:19px;color:var(--ink);line-height:1}

.section-title{position:absolute;top:324px;font-size:12px;font-weight:700;color:var(--orange);text-transform:uppercase}
.section-title.faq{text-transform:none}
.section-rule{position:absolute;top:351px;height:1px;background:var(--rule)}

.faq-list{position:absolute;left:115px;top:365px;width:346px;list-style:none}
.faq-item{height:41px;margin-bottom:10.2px;background:linear-gradient(180deg,var(--card-top),var(--card-bottom));border:1px solid var(--card-border);display:flex;align-items:center;font-size:9px;color:var(--text)}
.faq-item svg{width:8px;height:8px;margin:0 12px 0 7px;flex:none}
.more-btn{position:absolute;left:114px;top:1079px;width:83px;height:22px;background:var(--orange);color:#fff;font-size:9px;font-weight:700;display:flex;align-items:center;justify-content:center;gap:6px}

.video{position:absolute;left:477px;width:243px}
.video-thumb{position:relative;width:243px;height:150px}
.video-thumb .play{position:absolute;left:101px;top:55px;width:40px;height:40px}
.video-caption{font-size:9.5px;line-height:15px;color:var(--ink);margin-top:5px;width:240px}
.watch-btn{margin-top:5px;width:84px;height:21px;background:var(--orange);color:#fff;font-size:9px;font-weight:700;display:flex;align-items:center;justify-content:center;gap:5px}

.site-footer{position:absolute;left:0;top:1122px;width:837px;height:78px;background:var(--band);text-align:center;font-size:9.5px;color:var(--muted)}
.footer-links{margin-top:12px}
.footer-links span{margin:0 6px;color:#999}
.copyright{margin-top:5px}
.powered{margin-top:5px}
.powered strong{color:var(--orange);font-weight:700}
</style>
</head>
<body>
<header class="site-header">
  <div class="brand"><span class="brand-mark"></span>PixelHarbor</div>
  <div class="live-support">
    <svg width="14" height="11" viewBox="0 0 14 11"><ellipse cx="7" cy="5" rx="6.5" ry="4.5" fill="#fff"/><path d="M3 8 L2 11 L6 9Z" fill="#fff"/></svg>
    Live Support <span class="caret"></span>
  </div>
</header>

<section class="hero">
  <div class="hero-art left" role="img" aria-label="Illustration of a friendly repairman holding a wrench"></div>
  <h1 class="hero-title">Pixel Harbor <strong>Support</strong></h1>
  <p class="hero-sub">We are Happy To Help You !</p>
  <div class="hero-art right" role="img" aria-label="Illustration of a repairman raising a finger beside a speech bubble"></div>
</section>

<h2 class="section-title faq" style="left:115px">FAQ’s</h2>
<div class="section-rule" style="left:115px;width:347px"></div>
<h2 class="section-title" style="left:478px">Video Tutorials</h2>
<div class="section-rule" style="left:477px;width:243px"></div>

<ul class="faq-list">
  <li class="faq-item"><svg viewBox="0 0 8 8"><path d="M2 1 L5.5 4 L2 7" stroke="#555" stroke-width="1.6" fill="none"/></svg>Lorem ipsum dolor sit amet, consectetur adipisicing elit, sed do eiusmod ?</li>
  <li class="faq-item"><svg viewBox="0 0 8 8"><path d="M2 1 L5.5 4 L2 7" stroke="#555" stroke-width="1.6" fill="none"/></svg>Tempor incididunt ut labore et dolore magna aliqua. Ut enim ad minim ?</li>
  <li class="faq-item"><svg viewBox="0 0 8 8"><path d="M2 1 L5.5 4 L2 7" stroke="#555" stroke-width="1.6" fill="none"/></svg>veniam, quis nostrud exercitation ullamco laboris nisi ut aliquip ex ?</li>
  <li class="faq-item"><svg viewBox="0 0 8 8"><path d="M2 1 L5.5 4 L2 7" stroke="#555" stroke-width="1.6" fill="none"/></svg>ea commodo consequat. Duis aute irure dolor in reprehenderit ?</li>
  <li class="faq-item"><svg viewBox="0 0 8 8"><path d="M2 1 L5.5 4 L2 7" stroke="#555" stroke-width="1.6" fill="none"/></svg>in voluptate velit esse cillum dolore eu fugiat nulla pariatur ?</li>
  <li class="faq-item"><svg viewBox="0 0 8 8"><path d="M2 1 L5.5 4 L2 7" stroke="#555" stroke-width="1.6" fill="none"/></svg>Excepteur sint occaecat cupidatat non proident, sunt in culpa ?</li>
  <li class="faq-item"><svg viewBox="0 0 8 8"><path d="M2 1 L5.5 4 L2 7" stroke="#555" stroke-width="1.6" fill="none"/></svg>Qui officia deserunt mollit anim id est laborum. ?</li>
  <li class="faq-item"><svg viewBox="0 0 8 8"><path d="M2 1 L5.5 4 L2 7" stroke="#555" stroke-width="1.6" fill="none"/></svg>Lorem ipsum dolor sit amet, consectetur adipisicing elit, sed do eiusmod ?</li>
  <li class="faq-item"><svg viewBox="0 0 8 8"><path d="M2 1 L5.5 4 L2 7" stroke="#555" stroke-width="1.6" fill="none"/></svg>Tempor incididunt ut labore et dolore magna aliqua. Ut enim ad minim ?</li>
  <li class="faq-item"><svg viewBox="0 0 8 8"><path d="M2 1 L5.5 4 L2 7" stroke="#555" stroke-width="1.6" fill="none"/></svg>veniam, quis nostrud exercitation ullamco laboris nisi ut aliquip ex ?</li>
  <li class="faq-item"><svg viewBox="0 0 8 8"><path d="M2 1 L5.5 4 L2 7" stroke="#555" stroke-width="1.6" fill="none"/></svg>ea commodo consequat. Duis aute irure dolor in reprehenderit ?</li>
  <li class="faq-item"><svg viewBox="0 0 8 8"><path d="M2 1 L5.5 4 L2 7" stroke="#555" stroke-width="1.6" fill="none"/></svg>in voluptate velit esse cillum dolore eu fugiat nulla pariatur ?</li>
  <li class="faq-item"><svg viewBox="0 0 8 8"><path d="M2 1 L5.5 4 L2 7" stroke="#555" stroke-width="1.6" fill="none"/></svg>Excepteur sint occaecat cupidatat non proident, sunt in culpa ?</li>
  <li class="faq-item"><svg viewBox="0 0 8 8"><path d="M2 1 L5.5 4 L2 7" stroke="#555" stroke-width="1.6" fill="none"/></svg>Qui officia deserunt mollit anim id est laborum. ?</li>
</ul>
<div class="more-btn">FOR MORE <svg width="9" height="7" viewBox="0 0 9 7"><path d="M1 1.5 L4.5 5 L8 1.5" stroke="#fff" stroke-width="2" fill="none"/></svg></div>

<article class="video" style="top:365px">
  <div class="video-thumb" role="img" aria-label="Video still: a man climbing a tree above a mountain valley" style="background:linear-gradient(160deg,#c9d2d8 0%,#6f8a6a 45%,#3c4d35 100%)">
    <svg class="play" viewBox="0 0 40 40"><circle cx="20" cy="20" r="18" fill="#333" fill-opacity=".75" stroke="#fff" stroke-width="2"/><path d="M16 12 L29 20 L16 28Z" fill="#fff"/></svg>
  </div>
  <p class="video-caption">Sed ut perspiciatis unde omnis iste natus error sit volupta-tem accusantium doloremque laudantium</p>
  <div class="watch-btn">WATCH NOW <svg width="12" height="12" viewBox="0 0 12 12"><circle cx="6" cy="6" r="6" fill="#fff"/><path d="M4.5 3 L8.5 6 L4.5 9Z" fill="#f26a1b"/></svg></div>
</article>

<article class="video" style="top:601px">
  <div class="video-thumb" role="img" aria-label="Video still: a group of people gathered outdoors" style="background:linear-gradient(160deg,#7b7f86 0%,#8a5a3c 50%,#3b2f2a 100%)">
    <svg class="play" viewBox="0 0 40 40"><circle cx="20" cy="20" r="18" fill="#333" fill-opacity=".75" stroke="#fff" stroke-width="2"/><path d="M16 12 L29 20 L16 28Z" fill="#fff"/></svg>
  </div>
  <p class="video-caption">Sed ut perspiciatis unde omnis iste natus error sit volupta-tem accusantium doloremque laudantium</p>
  <div class="watch-btn">WATCH NOW <svg width="12" height="12" viewBox="0 0 12 12"><circle cx="6" cy="6" r="6" fill="#fff"/><path d="M4.5 3 L8.5 6 L4.5 9Z" fill="#f26a1b"/></svg></div>
</article>

<article class="video" style="top:834px">
  <div class="video-thumb" role="img" aria-label="Video still: a night market with a loaded pickup truck" style="background:linear-gradient(160deg,#2a2a2e 0%,#7a3b2a 45%,#4a4a48 100%)">
    <svg class="play" viewBox="0 0 40 40"><circle cx="20" cy="20" r="18" fill="#333" fill-opacity=".75" stroke="#fff" stroke-width="2"/><path d="M16 12 L29 20 L16 28Z" fill="#fff"/></svg>
  </div>
  <p class="video-caption">Sed ut perspiciatis unde omnis iste natus error sit volupta-tem accusantium doloremque laudantium</p>
  <div class="watch-btn">WATCH NOW <svg width="12" height="12" viewBox="0 0 12 12"><circle cx="6" cy="6" r="6" fill="#fff"/><path d="M4.5 3 L8.5 6 L4.5 9Z" fill="#f26a1b"/></svg></div>
</article>

<footer class="site-footer">
  <nav class="footer-links">Home<span>|</span>Contact Us<span>|</span>Affiliate Program<span>|</span>Privacy Policy<span>|</span>Site Terms and Conditions<span>|</span>About Us</nav>
  <p class="copyright">© Copyright 2014 Northbay Imaging Pte Ltd. All rights reserved.</p>
  <p class="powered">Powered by <strong>PixelHarbor</strong></p>
</footer>
</body>
</html>
```